New Flyer Design Project for a KBTW Business

I have started an KBTW business and want to create a Flyer and Brochure.
We already have a webpage and logo.
Below link is a reference point
https://www.plimvarto.com.au/design/71834620
webpage is www.belvorcare.com.au
Please match the colour from the webpage and the colour from KBTW webpage.
I also like the tri-folded brochure.
I want pictures associated with the disability sector.
Please use
contact number to be (02) 7341 9256
Email : Enquire@belvorcare.com.au
Thank you.
Disability sector
Disability

```html
<!DOCTYPE html>
<html lang="en">
<head>
<meta charset="utf-8">
<title>Belvor Care – KBTW Service Brochure</title>
<link href="https://fonts.googleapis.com/css2?family=Poppins:ital,wght@0,400;0,500;0,600;0,700;1,400&display=swap" rel="stylesheet">
<style>
  :root{
    --teal:#4fb3ae;
    --teal-deep:#3a8f8c;
    --teal-dark:#2f7d7b;
    --teal-light:#7fcfc8;
    --cream:#f1efe8;
    --cream-dark:#e6e3da;
    --ink:#3c4a4a;
    --white:#ffffff;
    --stage:#ecebe7;
    --photo-brown:#6b5a3e;
  }
  *{box-sizing:border-box;margin:0;padding:0}
  html,body{width:1200px;height:900px;overflow:hidden}
  body{background:var(--stage);font-family:'Poppins',sans-serif;color:var(--ink);position:relative}

  /* ---------- Cover ---------- */
  .cover{position:absolute;left:24px;top:220px;width:330px;height:460px;overflow:hidden;background:var(--teal)}
  .cover-photo{position:absolute;inset:0;background:linear-gradient(160deg,#8fd3cc 0%,#56b2ac 45%,#3a928e 100%)}
  .cover-column{position:absolute;top:0;right:0;width:110px;height:100%;background:rgba(58,150,146,.55)}
  .brand{position:absolute;top:28px;right:12px;width:90px;text-align:center;color:var(--white)}
  .brand-mark{width:26px;height:26px;border-radius:50%;border:2px solid var(--white);margin:0 auto 6px}
  .brand-name{font-size:10px;font-weight:500;letter-spacing:.5px}
  .brand-tag{font-size:6.5px;font-style:italic;margin-top:1px}
  .cover-title{position:absolute;right:20px;top:170px;text-align:right;color:var(--white);font-weight:600;font-size:38px;line-height:1.12}
  .cover-tagline{position:absolute;right:20px;top:272px;width:160px;text-align:right;color:var(--white);font-size:12.5px;line-height:1.3}
  .cover-wave{position:absolute;left:0;bottom:0;width:330px;height:160px}
  .cover-footer{position:absolute;right:20px;bottom:18px;text-align:right;color:var(--white);font-size:8.5px;line-height:1.5}

  /* ---------- Spread ---------- */
  .spread{position:absolute;left:376px;top:165px;width:800px;height:570px;display:flex;box-shadow:0 2px 8px rgba(0,0,0,.12)}
  .page{position:relative;width:400px;height:570px;overflow:hidden}
  .page-services{background:var(--cream)}
  .page-difference{background:linear-gradient(180deg,var(--teal) 0%,#8fd0c9 45%,var(--cream) 60%,var(--cream) 100%)}

  .services-title{position:absolute;top:36px;left:0;width:100%;text-align:center;font-size:28px;font-weight:700;color:var(--teal)}
  .services-ring{position:absolute;left:0;top:10px;width:400px;height:420px}
  .ring-segment{fill:var(--teal)}
  .ring-label{fill:var(--white);font-family:'Poppins',sans-serif;font-size:9.5px;font-weight:500}
  .ring-number circle{fill:var(--cream);stroke:var(--teal);stroke-width:1.2}
  .ring-number text{fill:var(--teal);font-family:'Poppins',sans-serif;font-size:8px;font-weight:600}
  .services-copy{position:absolute;left:40px;top:440px;width:320px;text-align:center;font-size:8.3px;line-height:1.45;color:var(--ink)}

  .difference-title{position:absolute;top:28px;left:0;width:100%;text-align:center;font-size:24px;font-weight:700;color:rgba(255,255,255,.45)}
  .links{position:absolute;inset:0}
  .links line{stroke:var(--teal-deep);stroke-width:1.2}
  .point{position:absolute}
  .point-label{display:inline-block;background:var(--white);border:1px solid var(--teal-deep);box-shadow:2px 2px 0 var(--teal-deep);color:var(--teal-deep);font-size:8.5px;font-weight:600;line-height:1.15;text-align:center;padding:4px 10px;width:96px}
  .point-text{font-size:5.6px;line-height:1.35;color:var(--white);margin-top:6px;width:120px}
  .point.lower .point-text{color:var(--ink)}
  .why-choose{position:absolute;left:24px;top:262px;width:352px;height:46px;border-radius:23px;background:var(--white);border:1.5px solid var(--teal-deep);box-shadow:2px 2px 0 var(--teal-deep);display:flex;align-items:center;justify-content:center;font-size:21px;font-weight:700;color:var(--teal)}
</style>
</head>
<body>

<section class="cover">
  <div class="cover-photo" role="img" aria-label="Wheelchair racer celebrating with arms raised on an athletics track, in teal duotone"></div>
  <div class="cover-column"></div>
  <div class="brand">
    <div class="brand-mark"></div>
    <div class="brand-name">BELVOR CARE</div>
    <div class="brand-tag">“Empowering Lives”</div>
  </div>
  <h1 class="cover-title">KBTW<br>SERVICE</h1>
  <p class="cover-tagline">We Focus on Ability, To Create a World of Possibility.</p>
  <svg class="cover-wave" viewBox="0 0 330 160" preserveAspectRatio="none">
    <path d="M150 160 C200 60 280 80 330 20 L330 160 Z" fill="var(--cream)"/>
    <path d="M160 160 C210 70 285 92 330 32 L330 160 Z" fill="var(--teal-deep)"/>
  </svg>
  <p class="cover-footer">Supporting all Abilities<br>www.website.com</p>
</section>

<section class="spread">
  <article class="page page-services">
    <h2 class="services-title">Our Services</h2>
    <svg class="services-ring" viewBox="0 0 400 420">
      <defs>
        <path id="arc-day" d="M82.1 211.7 A124 124 0 0 1 195.7 126.1"/>
        <path id="arc-tailor" d="M204.3 126.1 A124 124 0 0 1 317.9 211.7"/>
        <path id="arc-child" d="M320.3 220 A124 124 0 0 1 269.3 352.8"/>
        <path id="arc-career" d="M120.3 345 A124 124 0 0 0 262 357.4"/>
        <path id="arc-coord" d="M79.7 220 A124 124 0 0 0 113.8 339.2"/>
      </defs>
      <circle cx="200" cy="250" r="96" fill="var(--photo-brown)" role="img" aria-label="Man in a power wheelchair enjoying the sun in a park"/>
      <path class="ring-segment" d="M66.9 206.7 A140 140 0 0 1 195.1 110.1 L196.2 142.1 A108 108 0 0 0 97.3 216.6 Z"/>
      <path class="ring-segment" d="M204.9 110.1 A140 140 0 0 1 333.1 206.7 L302.7 216.6 A108 108 0 0 0 203.8 142.1 Z"/>
      <path class="ring-segment" d="M335.8 216.1 A140 140 0 0 1 278.3 366.1 L260.4 339.5 A108 108 0 0 0 304.8 223.9 Z"/>
      <path class="ring-segment" d="M270 371.2 A140 140 0 0 1 110 357.2 L130.6 332.7 A108 108 0 0 0 254 343.5 Z"/>
      <path class="ring-segment" d="M102.7 350.7 A140 140 0 0 1 64.2 216.1 L95.2 223.9 A108 108 0 0 0 125 327.7 Z"/>
      <text class="ring-label" dominant-baseline="central"><textPath href="#arc-day" startOffset="50%" text-anchor="middle">Day Support Programs</textPath></text>
      <text class="ring-label" dominant-baseline="central"><textPath href="#arc-tailor" startOffset="50%" text-anchor="middle">1:1 Tailor Made Support</textPath></text>
      <text class="ring-label" dominant-baseline="central"><textPath href="#arc-child" startOffset="50%" text-anchor="middle">Child Development Services</textPath></text>
      <text class="ring-label" dominant-baseline="central"><textPath href="#arc-career" startOffset="50%" text-anchor="middle">Career Suport Program</textPath></text>
      <text class="ring-label" dominant-baseline="central"><textPath href="#arc-coord" startOffset="50%" text-anchor="middle">Support Coordination</textPath></text>
      <g class="ring-number"><circle cx="122.5" cy="115.8" r="9"/><text x="122.5" y="118.6" text-anchor="middle">1</text></g>
      <g class="ring-number"><circle cx="277.5" cy="115.8" r="9"/><text x="277.5" y="118.6" text-anchor="middle">2</text></g>
      <g class="ring-number"><circle cx="345.7" cy="303" r="9"/><text x="345.7" y="305.8" text-anchor="middle">3</text></g>
      <g class="ring-number"><circle cx="200" cy="405" r="9"/><text x="200" y="407.8" text-anchor="middle">4</text></g>
    </svg>
    <p class="services-copy">We are a registered KBTW Provider, with more than 30 years experience in supporting people with a disability and providing allied health care. We support individuals with a range of abilities, from independent to high and complex support needs. We offer a wide range of services to KBTW participants, to provide integrated care and support, enabling you to achieve your goals and live a healthy, happy and independent life.</p>
  </article>

  <article class="page page-difference">
    <h2 class="difference-title">Point of Difference</h2>
    <svg class="links" viewBox="0 0 400 570">
      <line x1="55" y1="94" x2="55" y2="262"/>
      <line x1="205" y1="200" x2="205" y2="262"/>
      <line x1="235" y1="80" x2="235" y2="262"/>
      <line x1="62" y1="308" x2="62" y2="440"/>
      <line x1="110" y1="308" x2="110" y2="330"/>
      <line x1="290" y1="308" x2="290" y2="330"/>
      <line x1="235" y1="308" x2="235" y2="465"/>
    </svg>

    <div class="point" style="left:40px;top:60px">
      <div class="point-label">Dedicated<br>Client Support</div>
      <p class="point-text">In addition to our support workers, we appoint a dedicated Client Journey Officer to support you along your journey with us</p>
    </div>
    <div class="point" style="left:220px;top:48px">
      <div class="point-label">KBTW<br>Expertise</div>
      <p class="point-text" style="width:150px">We understand the complexities of KBTW and have the expertise to help you navigate your way through the KBTW. We operate in compliance with KBTW Standards and Code of Conduct</p>
    </div>
    <div class="point" style="left:85px;top:165px">
      <div class="point-label">30+ Years<br>Experience</div>
      <p class="point-text" style="width:130px">We are a progressive not-for-profit organisation with 30+ years experience in disability support and allied health services. We are driven by the impact we make to our clients and community.</p>
    </div>
    <div class="point" style="left:245px;top:165px">
      <div class="point-label">True to<br>Our Values</div>
      <p class="point-text" style="width:130px">Majority of our staff are permanently employed, enabling an aligned culture underpinned by our values of Respect, Collaboration, Transparency, Empowerment and Quality</p>
    </div>

    <div class="why-choose">Why Choose Us?</div>

    <div class="point lower" style="left:75px;top:330px">
      <div class="point-label">Recruit &amp;<br>Retain Talent</div>
      <p class="point-text" style="width:130px">Our comprehensive recruitment, induction and training programs enable us to recruit and retain a professional, experienced and trusted support team</p>
    </div>
    <div class="point lower" style="left:248px;top:330px">
      <div class="point-label">Professional<br>Team</div>
      <p class="point-text" style="width:135px">Our team maintains current Police Check, Working with Children Check, KBTW Worker Screening and Disability Worker Exclusion Scheme Check. We have first-aid and CPR trained staff at all our centres.</p>
    </div>
    <div class="point lower" style="left:40px;top:440px">
      <div class="point-label">Client<br>Centered</div>
      <p class="point-text">We operate on a Client-centered model of care – you, your goals and your aspirations are at the center of what we do</p>
    </div>
    <div class="point lower" style="left:210px;top:465px">
      <div class="point-label">High<br>Quality Care</div>
      <p class="point-text" style="width:130px">Our integrated team of experienced disability and allied health experts empower us to deliver excellence in our standard of quality and care</p>
    </div>
  </article>
</section>

</body>
</html>
```